Tooth whitening strip packaging

We have some 4 oral care products that want to completely rebrand and change their packaging

Target Market(s)

Everyone

Industry/Entity Type

Oral care

Other font styles liked:
• We like simple and elegant font

Requirements
Must have
• 1) elegant, high tech, cutting-edge technology look 2) all the products should have the same branding scheme 3) we want the amazing look of these packages increase our sales

```html
<!DOCTYPE html>
<html lang="en">
<head>
<meta charset="utf-8">
<title>Glimo Plaque Disclosing Gel Pen – Carton Dieline</title>
<link href="https://fonts.googleapis.com/css2?family=Montserrat:wght@300;400;600;700;800&display=swap" rel="stylesheet">
<style>
  :root {
    --cut-red: #e8333c;
    --brand-blue: #31a4d3;
    --dot-blue: #8fd0ea;
    --ink-grey: #555659;
    --silver: #d6d8da;
    --white: #ffffff;
  }
  html, body {
    margin: 0;
    padding: 0;
    width: 1200px;
    height: 873px;
    overflow: hidden;
    background: var(--white);
    font-family: "Montserrat", sans-serif;
  }
  .carton {
    position: relative;
    width: 1200px;
    height: 873px;
  }
  .dieline {
    position: absolute;
    left: 0;
    top: 0;
  }
  .label {
    position: absolute;
    margin: 0;
    white-space: nowrap;
  }
  .rotated-up {
    transform: translate(-50%, -50%) rotate(-90deg);
  }
  .rotated-down {
    transform: translate(-50%, -50%) rotate(90deg);
  }
  .benefit-text {
    color: var(--ink-grey);
    font-weight: 300;
    font-size: 11px;
    line-height: 10px;
    text-align: left;
  }
  .step-number {
    position: absolute;
    width: 15px;
    height: 15px;
    border-radius: 50%;
    background: var(--ink-grey);
    color: var(--white);
    font-weight: 700;
    font-size: 10px;
    line-height: 15px;
    text-align: center;
    transform: translate(-50%, -50%) rotate(-90deg);
  }
  .icon-slot {
    position: absolute;
    width: 36px;
    height: 36px;
    border-radius: 8px;
    background: var(--silver);
    transform: translate(-50%, -50%);
  }
  .divider {
    position: absolute;
    width: 2px;
    height: 26px;
    background: var(--ink-grey);
    transform: translate(-50%, -50%);
  }
  .easy-title {
    color: var(--ink-grey);
    font-weight: 700;
    font-size: 12px;
    line-height: 11px;
  }
  .count-figure {
    color: var(--ink-grey);
    font-weight: 400;
    font-size: 30px;
    line-height: 30px;
  }
  .brand-name {
    color: var(--silver);
    font-weight: 800;
    font-size: 44px;
    letter-spacing: -1px;
  }
  .side-brand {
    color: var(--white);
    font-weight: 800;
    font-size: 17px;
  }
  .headline {
    position: absolute;
    left: 625px;
    margin: 0;
    color: var(--white);
    font-weight: 800;
    font-size: 19px;
    line-height: 17px;
    letter-spacing: 0.2px;
  }
  .gel-pen-tag {
    display: inline-block;
    margin-top: 4px;
    padding: 0 4px;
    background: var(--silver);
    color: var(--brand-blue);
    font-weight: 600;
    font-size: 16px;
    line-height: 18px;
  }
  .claims {
    position: absolute;
    left: 625px;
    margin: 0;
    color: var(--white);
    font-weight: 600;
    font-size: 8.6px;
    letter-spacing: 0.2px;
    white-space: nowrap;
  }
  .volume {
    color: var(--white);
    font-weight: 700;
    font-size: 12px;
  }
  .benefit-strip {
    position: absolute;
    left: 268px;
    top: 516px;
    width: 673px;
    height: 21px;
    margin: 0;
    color: var(--white);
    font-weight: 400;
    font-size: 8.6px;
    line-height: 21px;
    text-align: center;
    word-spacing: 0.5px;
  }
</style>
</head>
<body>
<main class="carton">

  <svg class="dieline" width="1200" height="873" viewBox="0 0 1200 873" aria-hidden="true">
    <defs>
      <linearGradient id="halftone-glow" x1="0" x2="1" y1="0" y2="0">
        <stop offset="0" stop-color="var(--dot-blue)" stop-opacity="0.45"/>
        <stop offset="0.3" stop-color="var(--dot-blue)" stop-opacity="0"/>
        <stop offset="0.7" stop-color="var(--dot-blue)" stop-opacity="0"/>
        <stop offset="1" stop-color="var(--dot-blue)" stop-opacity="0.45"/>
      </linearGradient>
    </defs>

    <g fill="none" stroke="var(--cut-red)" stroke-width="1">
      <!-- top dust flaps -->
      <polyline points="268,180 253,180 239,195 213,195 213,283 247,283 268,299"/>
      <polyline points="941,180 956,180 970,195 996,195 996,283 962,283 941,299"/>
      <!-- bottom dust flaps -->
      <polyline points="268,418 247,434 213,434 213,522 239,522 253,537 268,537"/>
      <polyline points="941,418 962,434 996,434 996,522 970,522 956,537 941,537"/>
      <!-- rounded tuck flaps -->
      <path d="M150,299 C115,299 95,330 87,358 C95,386 115,418 150,418"/>
      <path d="M1059,299 C1094,299 1114,330 1122,358 C1114,386 1094,418 1059,418"/>
      <line x1="150" y1="325" x2="154" y2="325"/>
      <line x1="150" y1="392" x2="154" y2="392"/>
      <line x1="1055" y1="325" x2="1059" y2="325"/>
      <line x1="1055" y1="392" x2="1059" y2="392"/>
      <!-- glue flap -->
      <polyline points="268,656 284,708 925,708 941,656"/>
    </g>

    <!-- blue panels -->
    <g fill="var(--brand-blue)">
      <rect x="150" y="299" width="118" height="119"/>
      <rect x="268" y="299" width="673" height="119"/>
      <rect x="941" y="299" width="118" height="119"/>
      <rect x="268" y="516" width="673" height="21"/>
      <rect x="268" y="537" width="673" height="119"/>
    </g>
    <rect x="268" y="299" width="673" height="119" fill="url(#halftone-glow)" role="img" aria-label="Soft halftone dot texture"/>
    <rect x="268" y="537" width="673" height="119" fill="url(#halftone-glow)" role="img" aria-label="Soft halftone dot texture"/>

    <!-- panel outlines and fold lines -->
    <g fill="none" stroke="var(--cut-red)" stroke-width="1">
      <rect x="268" y="180" width="673" height="476"/>
      <rect x="150" y="299" width="909" height="119"/>
      <line x1="268" y1="299" x2="268" y2="418"/>
      <line x1="941" y1="299" x2="941" y2="418"/>
      <line x1="268" y1="537" x2="941" y2="537"/>
    </g>
  </svg>

  <!-- top panel: benefits -->
  <section class="benefits" aria-label="Product benefits">
    <div class="icon-slot" style="left:379px; top:240px;" role="img" aria-label="Gel pen icon"></div>
    <p class="label benefit-text rotated-up" style="left:426px; top:240px;">Easy<br>to use</p>
    <span class="divider" style="left:471px; top:240px;"></span>

    <p class="label count-figure rotated-up" style="left:515px; top:240px;">90</p>
    <p class="label benefit-text rotated-up" style="left:547px; top:240px;">90 times<br>of uses</p>
    <span class="divider" style="left:595px; top:240px;"></span>

    <div class="icon-slot" style="left:648px; top:240px;" role="img" aria-label="Hand holding pen icon"></div>
    <p class="label benefit-text rotated-up" style="left:695px; top:240px;">No more<br>messy<br>tablets</p>
    <span class="divider" style="left:751px; top:240px;"></span>

    <div class="icon-slot" style="left:805px; top:240px; border-radius:50%;" role="img" aria-label="Pleasant taste icon"></div>
    <p class="label benefit-text rotated-up" style="left:839px; top:240px;">Pleasant<br>taste</p>
  </section>

  <!-- side panels -->
  <p class="label side-brand rotated-down" style="left:209px; top:358px;">Glimo</p>
  <p class="label side-brand rotated-up" style="left:999px; top:358px;">Glimo</p>

  <!-- front panel -->
  <section class="front-face" aria-label="Front panel">
    <p class="label brand-name" style="left:364px; top:331px;">Glimo</p>
    <h1 class="headline" style="top:329px;">PLAQUE<br>DISCLOSING<br><span class="gel-pen-tag">GEL PEN</span></h1>
    <p class="claims" style="top:399px;">SAY NO TO CAVITIES | FDA APPROVED | SAFE INGREDIENTS</p>
    <p class="label volume rotated-up" style="left:918px; top:359px;">4ml</p>
  </section>

  <!-- bottom panel: directions -->
  <section class="directions" aria-label="Directions">
    <p class="label easy-title rotated-up" style="left:370px; top:467px;">Easy<br>to use:</p>

    <span class="step-number" style="left:431px; top:467px;">1</span>
    <div class="icon-slot" style="left:468px; top:467px;" role="img" aria-label="Teeth icon"></div>
    <p class="label benefit-text rotated-up" style="left:504px; top:467px;">Apply</p>
    <span class="divider" style="left:550px; top:467px;"></span>

    <span class="step-number" style="left:588px; top:467px;">2</span>
    <div class="icon-slot" style="left:621px; top:467px;" role="img" aria-label="Smile with teeth icon"></div>
    <p class="label benefit-text rotated-up" style="left:660px; top:467px;">See the<br>purple<br>plaque</p>
    <span class="divider" style="left:722px; top:467px;"></span>

    <span class="step-number" style="left:764px; top:467px;">3</span>
    <div class="icon-slot" style="left:807px; top:467px;" role="img" aria-label="Toothbrush and toothpaste icon"></div>
    <p class="label benefit-text rotated-up" style="left:844px; top:467px;">Brush</p>
  </section>

  <p class="benefit-strip">DETECTION OF DENTAL PLAQUE &nbsp;| &nbsp;CLEAN YOUR TEETH &nbsp;&nbsp;| &nbsp;FRESH BREATH &nbsp;| &nbsp;&nbsp;REDUCES PLAQUE</p>

  <!-- back panel -->
  <section class="back-face" aria-label="Back panel">
    <p class="label brand-name" style="left:364px; top:569px;">Glimo</p>
    <h2 class="headline" style="top:567px;">PLAQUE<br>DISCLOSING<br><span class="gel-pen-tag">GEL PEN</span></h2>
    <p class="claims" style="top:637px;">SAY NO TO CAVITIES | FDA APPROVED | SAFE INGREDIENTS</p>
    <p class="label volume rotated-up" style="left:918px; top:597px;">4ml</p>
  </section>

</main>
</body>
</html>
```